trading data display webpage

We have build a rough wireframe of the two webpages that we want to display .The two wireframes are attached as a pdf document.
there will be login page. after login , the user will see the index page. that is the first page of the wireframe.

what we are displaying is essentially spread data. we are taking the difference in prices are two places and displaying the data. some calculations are done and is shown in the grid.

below the grid we show the behaviour on a graph. we will use bubble chart. I did not find a sample, hence have thrown in a placeholder.

this is time series data ( changes daily) and hence we need to check the behaviour.

the second wire frame shows how the user will choose the source price points and the destination price points.
we are talking here of natural gas prices hence the reference to source prices and destination prices.

you need to design the page/ pages such that the end-user loves it and is easy to use. the intent here is easy to use and easy to understand.
this will be responsive webpage since the end user will check it out on a tablet or a smartphone.

so if possible tell us how the navigation bar, the button bar, etc should fall when the screen size decreases.

I have uploaded 2 files. one is the wireframe ( pdf document) and second is the logo file.

please also let us know where to place the logo.

Target Market(s)

the target market is traders and data analyst

Industry/Entity Type

Build

Colors

Designer to choose colors to be used in the design.

Requirements
Must have
• 1. design for the web.
2. but think how the design will look when the screen size decreases.
3. tell if possible what screen components to keep and what to hide.

```html
<!DOCTYPE html>
<html lang="en">
<head>
<meta charset="utf-8">
<title>Spreadline – Spread Dashboard</title>
<link href="https://fonts.googleapis.com/css2?family=Roboto:wght@300;400;500;700&display=swap" rel="stylesheet">
<style>
:root{
  --bg:#f3f4f6;
  --panel:#ffffff;
  --line:#dcdde0;
  --text:#333638;
  --muted:#7b7f84;
  --green:#8cc63f;
  --green-dark:#6aa130;
  --green-light:#cfe6ab;
  --orange:#f26a23;
  --orange-light:#fbe0d3;
  --pink:#ee1660;
  --row-alt:#f4f4f5;
  --band:#f7f7f8;
}
*{box-sizing:border-box;margin:0;padding:0}
html,body{width:1200px;height:1029px;overflow:hidden}
body{background:var(--bg);font-family:'Roboto',sans-serif;color:var(--text);position:relative}
.abs{position:absolute}
.brand{left:99px;top:40px;display:flex;align-items:center;gap:10px;font-size:30px;font-weight:700;color:var(--green)}
.brand-dot{width:30px;height:30px;border-radius:50%;background:var(--orange)}
.user-nav{right:112px;top:37px;display:flex;font-size:11px;color:#444}
.user-nav a{color:inherit;text-decoration:none;padding:0 10px;border-left:1px solid #ccc;display:flex;align-items:center;gap:5px}
.user-nav a:first-child{border-left:none}
.user-nav svg{width:13px;height:13px;fill:#555}
.region-tab{top:88px;height:43px;display:flex;align-items:center;justify-content:center;font-size:13px;font-weight:700;color:#fff;letter-spacing:.3px}
.tab-east{left:649px;width:136px;background:var(--panel);color:var(--green);border-radius:4px 4px 0 0;box-shadow:0 -1px 3px rgba(0,0,0,.08);top:87px;height:44px;padding-bottom:6px}
.tab-central{left:791px;width:170px;background:var(--orange);border-radius:3px 3px 0 0}
.tab-west{left:967px;width:135px;background:var(--pink);border-radius:3px 3px 0 0}
.panel{left:99px;top:130px;width:1003px;height:772px;background:var(--panel);box-shadow:0 1px 3px rgba(0,0,0,.06)}
.select{top:147px;width:282px;height:44px;border:1px solid var(--line);background:#fff;display:flex;align-items:center;justify-content:space-between;padding:0 20px 0 17px;font-size:17px;color:#333}
.select i{width:0;height:0;border-left:7px solid transparent;border-right:7px solid transparent;border-top:7px solid #555}
.seg{top:212px;height:43px;display:flex;border:1px solid var(--line);border-radius:3px;overflow:hidden}
.seg span{flex:1;display:flex;align-items:center;justify-content:center;font-size:13px;color:#444;background:linear-gradient(#fff,#f5f5f5);border-left:1px solid var(--line)}
.seg span:first-child{border-left:none}
.seg span.on{background:linear-gradient(#8cc63f,#6aa130);color:#fff;font-weight:700}
.spread-table{left:115px;top:280px;width:973px;border-collapse:collapse;font-size:13px}
.spread-table th,.spread-table td{border:1px solid var(--line);height:43px;padding:0 17px;text-align:left}
.spread-table th{font-weight:500;background:#f7f7f8}
.spread-table tr:nth-child(even) td{background:var(--row-alt)}
.spread-table td.dash{letter-spacing:2px;color:#555;padding-left:15px}
.chart-band{top:578px;height:71px;background:var(--band)}
.chart-title{font-size:12.5px;font-weight:700;letter-spacing:.2px}
.divider{left:602px;top:578px;width:1px;height:324px;background:#ececee}
.copy-head{left:361px;top:713px;font-size:12.5px;font-weight:700;color:#666}
.copy-body{left:361px;top:740px;width:225px;font-size:11px;line-height:13.4px;color:#777}
.learn{left:361px;top:841px;font-size:11px;font-weight:700;color:var(--green)}
.gauge-num{left:198px;top:726px;font-size:49px;font-weight:300;color:var(--green)}
.gauge-num sup{font-size:27px;vertical-align:top;position:relative;top:4px}
.gauge-label{left:193px;top:786px;font-size:10.5px;color:var(--green)}
.footer{left:101px;top:920px;font-size:11px;color:#777;line-height:19px}
.footer nav a{color:inherit;text-decoration:none}
.footer nav span{margin:0 9px;color:#999}
.social{right:104px;top:922px;display:flex;gap:19px}
.social i{width:12px;height:12px;border-radius:50%;background:#b5b8bc}
</style>
</head>
<body>

<div class="abs brand"><span class="brand-dot"></span>Spreadline</div>

<nav class="abs user-nav">
  <a href="#"><svg viewBox="0 0 16 16"><circle cx="8" cy="8" r="5"/><circle cx="8" cy="8" r="2" fill="#fff"/><rect x="7" y="0" width="2" height="16"/><rect x="0" y="7" width="16" height="2"/></svg>My Account</a>
  <a href="#"><svg viewBox="0 0 16 16"><circle cx="8" cy="8" r="7" fill="none" stroke="#555" stroke-width="1.5"/><rect x="7.2" y="6.5" width="1.6" height="5"/><rect x="7.2" y="3.8" width="1.6" height="1.6"/></svg>Help Centre</a>
  <a href="#"><svg viewBox="0 0 16 16"><path d="M2 2h9v3h-2V4H4v8h5v-1h2v3H2z"/><path d="M6 7h6V5l3 3-3 3V9H6z"/></svg>Log out</a>
  <a href="#"><svg viewBox="0 0 16 16"><circle cx="8" cy="5" r="3.5"/><path d="M1 15c0-4 3-6 7-6s7 2 7 6z"/></svg>Hi! User</a>
</nav>

<div class="abs region-tab tab-central">CENTRAL</div>
<div class="abs region-tab tab-west">WEST</div>
<div class="abs panel"></div>
<div class="abs region-tab tab-east">EAST</div>

<div class="abs select" style="left:115px">Source Indices<i></i></div>
<div class="abs select" style="left:806px">Destination Indices<i></i></div>

<div class="abs seg" style="left:115px;width:569px"><span>5 days</span><span class="on">7 days</span><span>18 days</span></div>
<div class="abs seg" style="left:707px;width:381px;border-radius:0"><span>Month</span><span class="on">Year</span></div>

<table class="abs spread-table">
  <colgroup><col style="width:171px"><col style="width:124px"><col style="width:124px"><col style="width:124px"><col style="width:124px"><col style="width:123px"><col></colgroup>
  <tr><th>Spread-name</th><th>Avg sprd</th><th>+ve prob</th><th>-ve prob</th><th>Spike prob</th><th>Avg supply</th><th>Supply cut_prob</th></tr>
  <tr><td>Spread 1</td><td>Item 1</td><td class="dash">----</td><td class="dash">----</td><td class="dash">----</td><td class="dash">----</td><td class="dash">----</td></tr>
  <tr><td>Spread 2</td><td>Item 2</td><td class="dash">----</td><td class="dash">----</td><td class="dash">----</td><td class="dash">----</td><td class="dash">----</td></tr>
  <tr><td>Spread 3</td><td>Item 3</td><td class="dash">----</td><td class="dash">----</td><td class="dash">----</td><td class="dash">----</td><td class="dash">----</td></tr>
  <tr><td>Spread 4</td><td>Item 4</td><td class="dash">----</td><td class="dash">----</td><td class="dash">----</td><td class="dash">----</td><td class="dash">----</td></tr>
  <tr><td>Spread 5</td><td>Item 5</td><td class="dash">----</td><td class="dash">----</td><td class="dash">----</td><td class="dash">----</td><td class="dash">----</td></tr>
</table>

<div class="abs chart-band" style="left:115px;width:487px"></div>
<div class="abs chart-band" style="left:603px;width:485px"></div>
<div class="abs divider"></div>
<div class="abs chart-title" style="left:453px;top:610px;color:var(--green)">SPREAD V/S SUPPLY</div>
<div class="abs chart-title" style="left:914px;top:609px;color:var(--orange)">SPREADS ACROSS TIME</div>

<svg class="abs" style="left:0;top:0" width="1200" height="1029" viewBox="0 0 1200 1029" aria-hidden="true">
  <ellipse cx="240" cy="659" rx="64" ry="24" fill="#fff"/>
  <rect x="170" y="650" width="140" height="10" fill="#fff"/>
  <path d="M208.2,679.6 A93,93 0 0 1 291.3,844.6" fill="none" stroke="#d4d6d9" stroke-width="10" stroke-dasharray="1.2 1.6"/>
  <circle cx="291.3" cy="844.6" r="9" fill="#fff" stroke="#d4d6d9" stroke-width="4" stroke-dasharray="1.2 1.6"/>
  <path d="M149.4,746.1 A93,93 0 0 1 197.8,684.1" fill="none" stroke="var(--green-light)" stroke-width="7"/>
  <path d="M187.4,843.6 A93,93 0 0 1 149.4,746.1" fill="none" stroke="var(--green)" stroke-width="7"/>
  <circle cx="187.4" cy="843.6" r="10" fill="var(--green)"/>
  <circle cx="187.4" cy="843.6" r="4" fill="#fff"/>
</svg>
<div class="abs gauge-num">30<sup>%</sup></div>
<div class="abs gauge-label">SPREAD V/S SUPPLY</div>

<div class="abs copy-head">LOREM IPSUM DOLOR</div>
<p class="abs copy-body">Lorem ipsum dolor sit amet, consectetuer adipiscing elit, sed diam nonummy nibh euismod tincidunt ut laoreet dolore magna aliquam erat volutpat. Ut wisi enim ad minim veniam, quis nostrud exerci tation ullamcorper suscipit lobortis nisl ut aliquip ex ea commodo consequat.</p>
<a class="abs learn">Learn more...</a>

<svg class="abs" style="left:620px;top:665px" width="440" height="215" viewBox="0 0 440 215" role="img" aria-label="Bar chart of spreads from December 2013 to December 2014">
  <g stroke="#ececee" stroke-width="1">
    <line x1="21" y1="26" x2="434" y2="26"/><line x1="21" y1="60" x2="434" y2="60"/><line x1="21" y1="93" x2="434" y2="93"/><line x1="21" y1="127" x2="434" y2="127"/><line x1="21" y1="160" x2="434" y2="160"/>
  </g>
  <line x1="21" y1="9" x2="21" y2="193" stroke="#aaa"/>
  <line x1="21" y1="193" x2="434" y2="193" stroke="#aaa"/>
  <g font-family="Roboto,sans-serif" font-size="11" fill="#777" text-anchor="end">
    <text x="12" y="30">5</text><text x="12" y="64">4</text><text x="12" y="97">3</text><text x="12" y="131">2</text><text x="12" y="164">1</text>
  </g>
  <g fill="var(--green-light)"><rect x="46" y="131" width="15.5" height="62"/><rect x="69" y="121" width="15.5" height="72"/><rect x="92" y="121" width="15.5" height="72"/><rect x="115" y="121" width="15.5" height="72"/></g>
  <g fill="#f2f2f3"><rect x="139" y="95" width="15.5" height="98"/><rect x="162" y="95" width="15.5" height="98"/><rect x="185" y="95" width="15.5" height="98"/><rect x="208" y="95" width="15.5" height="98"/></g>
  <g fill="var(--orange-light)"><rect x="231" y="74" width="15.5" height="119"/><rect x="254" y="60" width="15.5" height="133"/><rect x="277" y="60" width="15.5" height="133"/><rect x="300" y="60" width="15.5" height="133"/></g>
  <g fill="var(--orange)"><rect x="324" y="26" width="15.5" height="167"/><rect x="347" y="26" width="15.5" height="167"/><rect x="370" y="26" width="15.5" height="167"/><rect x="393" y="26" width="15.5" height="167"/></g>
  <g font-family="Roboto,sans-serif" font-size="11" fill="#777"><text x="19" y="210">1- dec- 2013</text><text x="434" y="210" text-anchor="end">1- dec- 2014</text></g>
</svg>

<footer class="abs footer">
  <p>Copyright © 2014 Spreadline. All rights Reserved.</p>
  <nav><a href="#">Sitemap</a><span>|</span><a href="#">Logout</a><span>|</span><a href="#">Contact us</a><span>|</span><a href="#">Privacy Policy</a><span>|</span><a href="#">Blog</a><span>|</span><a href="#">Help centre</a></nav>
</footer>
<div class="abs social"><i></i><i></i><i></i></div>

</body>
</html>
```